FLYER: Human Factors in Traffic Crashes - Analysis of Drivers' Responses - training

We are hosting a class in Australia 30, November to 4, December 2020. I would like to have a flyer designed to "sell" the class with description of course topics. I have uploaded a flyer I started on my own but I want it to be professional. Dr. Pelloway only gets to AU every 3-5 years to teach from the US. I would like to have some type of roadway scenery, prefer a nighttime scene.

Target Market(s)

Accident reconstructionists and engineers, police reconstructionists.

Font styles to use
Serif

Colors
fec214

Requirements
Must have
• Name of course and course topics, location of course, price, website and contact information.
Nice to have
• Some type of roadway background, possibly a nighttime scene on a roadway.

```html
<!DOCTYPE html>
<html lang="en">
<head>
<meta charset="utf-8">
<title>Human Factors in Traffic Crashes – Course Flyer</title>
<link href="https://fonts.googleapis.com/css2?family=Oswald:wght@500;600&family=Barlow+Semi+Condensed:wght@400;600;700&display=swap" rel="stylesheet">
<style>
  :root {
    --yellow: #fec214;
    --ink: #0d0d0f;
    --night: #2a2a33;
    --haze: #4a4a58;
    --white: #ffffff;
    --muted: #d8d8dc;
    --stage: #8c8c8c;
  }
  * { box-sizing: border-box; margin: 0; padding: 0; }
  html, body { width: 856px; height: 1200px; overflow: hidden; }
  body { background: var(--stage); font-family: "Barlow Semi Condensed", sans-serif; }

  .flyer {
    position: absolute; left: 0; top: 44px; width: 856px; height: 1111px;
    background: radial-gradient(ellipse 70% 40% at 45% 68%, var(--haze) 0%, var(--night) 45%, var(--ink) 100%);
    overflow: hidden; color: var(--white);
  }
  .hazard-band { position: absolute; left: 0; top: 0; width: 856px; height: 24px; }

  .course-title {
    position: absolute; top: 58px; left: 0; width: 856px; text-align: center;
    font-family: "Oswald", sans-serif; font-weight: 600; color: var(--yellow);
    font-size: 47px; line-height: 66px; letter-spacing: 0.5px; text-transform: uppercase;
    white-space: nowrap;
  }

  .topics {
    position: absolute; z-index: 2; left: 44px; top: 213px; width: 358px; height: 562px;
    border: 1.5px solid var(--yellow); background: rgba(20,20,24,0.55);
  }
  .topics-header {
    background: var(--yellow); color: var(--ink); height: 42px; text-align: center;
    font-weight: 700; font-size: 22px; line-height: 42px; letter-spacing: 1.5px;
  }
  .topics-body { padding: 14px 18px 0 18px; }
  .topic-group-title { color: var(--yellow); font-weight: 700; font-size: 15px; line-height: 20px; margin-bottom: 2px; }
  .topic-group + .topic-group { margin-top: 18px; }
  .topic-list { list-style: none; }
  .topic-list li {
    position: relative; padding-left: 28px; font-size: 14.5px; line-height: 21px; color: var(--muted);
  }
  .topic-list li .arrow { position: absolute; left: 0; top: 6px; }

  .details { position: absolute; z-index: 2; left: 439px; top: 210px; width: 390px; }
  .class-heading {
    font-family: "Oswald", sans-serif; font-weight: 500; font-size: 36px; line-height: 48px;
    letter-spacing: 1px; text-transform: uppercase; white-space: nowrap; margin-bottom: 12px;
  }
  .label { color: var(--yellow); font-weight: 700; font-size: 17px; line-height: 21px; }
  .presenter-name { color: var(--white); }
  .value { font-size: 17px; line-height: 21px; color: var(--white); white-space: nowrap; }
  .venue-photo {
    width: 349px; height: 96px; margin: 12px 0 24px;
    background: linear-gradient(100deg, #6d7a6a 0%, #9aa08f 30%, #2f8fa8 55%, #1a6f8c 100%);
  }
  .fee-line { font-size: 17px; line-height: 21px; }
  .fee-line strong { font-weight: 700; margin-right: 8px; }
  .block { margin-bottom: 14px; }
  .note { font-size: 15px; line-height: 21px; color: var(--muted); margin-top: 14px; width: 360px; }
  .divider { height: 1.5px; background: var(--yellow); width: 349px; margin: 16px 0 18px; }
  .phone { font-size: 25px; line-height: 32px; font-weight: 600; margin-top: 8px; letter-spacing: 0.5px; }

  .cityscape { position: absolute; z-index: 1; left: 0; top: 760px; width: 856px; height: 240px;
    background: linear-gradient(180deg, rgba(13,13,15,0) 0%, rgba(20,20,26,0.85) 40%, #1a1a20 100%); }
  .road { position: absolute; z-index: 1; left: 0; top: 985px; width: 856px; height: 50px; }

  .brand-tile {
    position: absolute; z-index: 3; left: 0; top: 892px; width: 391px; height: 159px;
    background: var(--white); border-top-right-radius: 40px;
    display: flex; align-items: center; gap: 12px; padding-left: 34px;
  }
  .brand-mark { width: 22px; height: 22px; border-radius: 50%; background: var(--yellow); flex: none; }
  .brand-name { color: var(--ink); font-weight: 700; font-size: 32px; line-height: 34px; text-transform: uppercase; }

  .footer-band {
    position: absolute; z-index: 3; left: 0; bottom: 0; width: 856px; height: 60px; background: var(--yellow);
    color: var(--ink); text-align: center; font-size: 16px; line-height: 60px;
  }
  .footer-band strong { font-weight: 700; }
</style>
</head>
<body>
<main class="flyer">
  <svg class="hazard-band" viewBox="0 0 856 24" aria-hidden="true">
    <rect width="856" height="24" fill="#0d0d0f"/>
    <g fill="#fec214">
      <polygon points="30,4 90,4 80,20 20,20"/>
      <polygon points="135,4 195,4 185,20 125,20"/>
      <polygon points="240,4 300,4 290,20 230,20"/>
      <polygon points="345,4 405,4 395,20 335,20"/>
      <polygon points="450,4 510,4 500,20 440,20"/>
      <polygon points="555,4 615,4 605,20 545,20"/>
      <polygon points="660,4 720,4 710,20 650,20"/>
      <polygon points="765,4 825,4 815,20 755,20"/>
    </g>
  </svg>

  <h1 class="course-title">Human Factors in Traffic Crashes,<br>Analysis of Drivers’ Responses</h1>

  <section class="topics">
    <h2 class="topics-header">COURSE TOPICS</h2>
    <div class="topics-body">
      <div class="topic-group">
        <h3 class="topic-group-title">Perception-Response Time</h3>
        <ul class="topic-list">
          <li><svg class="arrow" width="14" height="10" viewBox="0 0 14 10" aria-hidden="true"><path d="M0 5h11M7 1l4 4-4 4" stroke="#fec214" stroke-width="2" fill="none"/></svg>Response to slow moving or stopped vehicles on multilane high speed roads</li>
          <li><svg class="arrow" width="14" height="10" viewBox="0 0 14 10" aria-hidden="true"><path d="M0 5h11M7 1l4 4-4 4" stroke="#fec214" stroke-width="2" fill="none"/></svg>Nighttime recognition</li>
          <li><svg class="arrow" width="14" height="10" viewBox="0 0 14 10" aria-hidden="true"><path d="M0 5h11M7 1l4 4-4 4" stroke="#fec214" stroke-width="2" fill="none"/></svg>Headlight mapping demonstration and instruction</li>
          <li><svg class="arrow" width="14" height="10" viewBox="0 0 14 10" aria-hidden="true"><path d="M0 5h11M7 1l4 4-4 4" stroke="#fec214" stroke-width="2" fill="none"/></svg>Driver decision making</li>
          <li><svg class="arrow" width="14" height="10" viewBox="0 0 14 10" aria-hidden="true"><path d="M0 5h11M7 1l4 4-4 4" stroke="#fec214" stroke-width="2" fill="none"/></svg>Research in IDRR</li>
          <li><svg class="arrow" width="14" height="10" viewBox="0 0 14 10" aria-hidden="true"><path d="M0 5h11M7 1l4 4-4 4" stroke="#fec214" stroke-width="2" fill="none"/></svg>Gap acceptance for left turns, right turns, and through movements for drivers, riders, and pedestrians</li>
          <li><svg class="arrow" width="14" height="10" viewBox="0 0 14 10" aria-hidden="true"><path d="M0 5h11M7 1l4 4-4 4" stroke="#fec214" stroke-width="2" fill="none"/></svg>Pedestrian walking speeds</li>
        </ul>
      </div>
      <div class="topic-group">
        <h3 class="topic-group-title">Acceleration</h3>
        <ul class="topic-list">
          <li><svg class="arrow" width="14" height="10" viewBox="0 0 14 10" aria-hidden="true"><path d="M0 5h11M7 1l4 4-4 4" stroke="#fec214" stroke-width="2" fill="none"/></svg>Lateral acceleration (swerving) for cars, motorcycles, and commercial vehicles</li>
          <li><svg class="arrow" width="14" height="10" viewBox="0 0 14 10" aria-hidden="true"><path d="M0 5h11M7 1l4 4-4 4" stroke="#fec214" stroke-width="2" fill="none"/></svg>Forward and backward acceleration of cars, motorcycles and commercial vehicles</li>
          <li><svg class="arrow" width="14" height="10" viewBox="0 0 14 10" aria-hidden="true"><path d="M0 5h11M7 1l4 4-4 4" stroke="#fec214" stroke-width="2" fill="none"/></svg>Drivers’ responses to green and yellow traffic signals, deceleration choice, reaction time and probability of stopping</li>
        </ul>
      </div>
    </div>
  </section>

  <section class="details">
    <h2 class="class-heading">Open Class:&nbsp; Manley NSW</h2>
    <p class="label">Presented by: <span class="presenter-name">Daniel Pelloway Ph.D.</span></p>
    <p class="value">World renowned Human Factors expert</p>
    <div class="venue-photo" role="img" aria-label="Aerial photo of the coastal headland venue beside a turquoise bay"></div>
    <div class="block">
      <p class="label">Location:</p>
      <p class="value">Harbourpoint Lodge – Coastal Headland Reserve</p>
      <p class="value">12 Seacliff Point Road, Manley NSW</p>
    </div>
    <p class="label">Course Fee:</p>
    <p class="fee-line"><strong>$1,730 AU</strong> $1,200 USD</p>
    <p class="note">It has been 3 years since Dr. Pelloway has come to AU to teach, don’t miss out on this year’s class.</p>
    <div class="divider"></div>
    <p class="label">Register on our website:</p>
    <p class="value">www.roadwisesafety.com or</p>
    <p class="label">Contact:</p>
    <p class="value">Dana@roadwisesafety.com</p>
    <p class="phone">555-014-2290</p>
  </section>

  <div class="cityscape" role="img" aria-label="Night city skyline silhouette above a dark roadway with oncoming headlights"></div>

  <svg class="road" viewBox="0 0 856 50" aria-hidden="true">
    <line x1="0" y1="6" x2="856" y2="6" stroke="#fec214" stroke-width="1.5"/>
    <line x1="400" y1="25" x2="856" y2="25" stroke="#ffffff" stroke-width="2" stroke-dasharray="22 14"/>
    <line x1="0" y1="44" x2="856" y2="44" stroke="#fec214" stroke-width="1.5"/>
  </svg>

  <div class="brand-tile">
    <span class="brand-mark"></span>
    <span class="brand-name">Roadwise<br>Safety Group</span>
  </div>

  <footer class="footer-band">Visit <strong>www.RoadwiseResearch.com/about/</strong> to learn more about Dr. Pelloway</footer>
</main>
</body>
</html>
```